Landing page for a cyber security service provider called 'Lumen Grove'

The client is a new cyber security company in need of a website landing page at lumengrove.example.

Their visual identity is modern, playful, clean and uncluttered and represents innovation, connectivity and approachability.

The company logo is provided in black (attached) but the client is open to changing the colour to align with the new website design.

The landing page needs to contain:
- A call to action with a 'Get Started' button
-Links to blank 'How it works', 'Products', 'Pricing', 'About Us' and 'Contact Us' pages (that we'll fill out later)

Target Market(s)

Medium to large businesses who probably don't understand cyber / cyber security but need their business to be protected.

Industry/Entity Type

Cyber Security

Coding

Coded - Design and coding required

Number of Pages Required

1 page

Font styles to use
Sans Serif
Other font styles liked:
• Helvetica

Requirements
Nice to have
• Hero banner at the top of the landing page.
Should not have
• Should not look like a traditional cyber / cyber security design (eg no dark blue/ black, red/black colour combinations). Please no military styles (eg no shields, cannons, swords, guns)

```html
<!DOCTYPE html>
<html lang="en">
<head>
<meta charset="utf-8">
<title>Lumen Grove — Cyber Security</title>
<link href="https://fonts.googleapis.com/css2?family=Arimo:wght@400;700&display=swap" rel="stylesheet">
<style>
:root{
  --teal:#0d5f5a;
  --teal-soft:#9cbfbf;
  --teal-pale:#b6d0ce;
  --mist:#d5e3e3;
  --mist-2:#c7d8d8;
  --sun:#fdc96b;
  --stone:#bdbbbb;
  --ink:#111;
  --grey:#666;
  --text:#444;
  --page:#f5f5f5;
  --card:#e8e8e8;
  --white:#fff;
}
*{margin:0;padding:0;box-sizing:border-box}
html,body{width:1200px;height:3790px;overflow:hidden}
body{background:var(--page);font-family:"Arimo",Helvetica,Arial,sans-serif;color:var(--ink);position:relative}
a{color:inherit;text-decoration:none}
.abs{position:absolute}

/* hero */
.hero{position:absolute;left:0;top:0;width:1200px;height:650px}
.hero-bg{position:absolute;inset:0;background:linear-gradient(100deg,#2a2d2a 0%,#3b3f3a 45%,#5d6561 70%,#4a4d4b 100%)}
.hero-wave{position:absolute;left:0;top:470px}
.brand{position:absolute;display:flex;align-items:center;gap:14px;color:var(--white);font-size:44px;font-weight:700;letter-spacing:.5px}
.brand .dot{width:34px;height:34px;border-radius:50%;background:var(--white)}
.nav{position:absolute;left:600px;top:46px;display:flex;gap:23px;font-size:14px;color:var(--white)}
.nav a.active{border-bottom:2px solid #3aa79e;padding-bottom:5px}
.hero-title{position:absolute;left:104px;top:168px;font-size:88px;font-weight:700;color:var(--white);line-height:1}
.hero-sub{position:absolute;left:395px;top:258px;font-size:27px;font-weight:700;color:var(--white)}
.hero-text{position:absolute;left:109px;top:310px;width:570px;font-size:20px;line-height:25px;color:var(--white)}
.btn-light{position:absolute;left:107px;top:412px;width:187px;height:47px;background:var(--white);color:var(--ink);font-size:15px;font-weight:700;display:flex;align-items:center;justify-content:center}

/* approach */
.approach-title{position:absolute;left:110px;top:728px;font-size:84px;font-weight:700;color:var(--grey);line-height:1}
.approach-title span,.approach-sub span{color:var(--teal)}
.approach-sub{position:absolute;left:110px;top:818px;font-size:37px;font-weight:700;color:var(--grey)}
.stat{position:absolute;display:flex;flex-direction:column;align-items:center;justify-content:center;color:var(--white)}
.stat b{font-size:70px;line-height:1}
.stat small{font-size:13px;font-weight:700;margin-top:4px}

/* about */
.about-panel{position:absolute;left:0;top:1022px;width:497px;height:563px;background:var(--teal-soft);border-radius:0 90px 90px 0}
.about-photo{position:absolute;left:110px;top:933px;width:355px;height:652px;background:linear-gradient(180deg,#8a7f74 0%,#3c4a63 45%,#2e3a52 100%);border-radius:140px 140px 0 0}
.about-title{position:absolute;left:564px;top:1034px;font-size:74px;font-weight:700;line-height:1}
.about-text{position:absolute;left:567px;top:1115px;width:530px;font-size:22px;line-height:29px;color:var(--text)}
.feature{position:absolute;left:567px;width:526px;height:146px;background:var(--teal-pale);border-radius:22px;padding:20px 20px 0 22px;color:var(--white)}
.feature h3{font-size:23px;margin-bottom:10px}
.feature p{font-size:18px;line-height:23px;color:#eef5f4}

/* how it works */
.how-title{position:absolute;left:104px;top:1700px;font-size:74px;font-weight:700;line-height:1}
.how-text{position:absolute;left:107px;top:1784px;width:470px;font-size:22px;line-height:29px;color:var(--text)}
.step{position:absolute;left:107px;width:490px}
.step h3{font-size:28px;font-weight:700;margin-bottom:10px}
.step p{font-size:19px;line-height:29px;color:var(--text)}
.rule{position:absolute;left:107px;width:490px;height:5px;background:#7fb5b0}
.how-photo{position:absolute;left:632px;top:1698px;width:568px;height:566px;border-radius:90px 0 0 90px;background:linear-gradient(120deg,#9cbfbf 0%,#5e7f95 35%,#2b4868 60%,#1d3551 100%)}

/* section heads */
.eyebrow{position:absolute;left:0;width:1200px;text-align:center;font-size:19px;color:var(--text)}
.sec-title{position:absolute;left:0;width:1216px;text-align:center;font-size:41px;font-weight:700}
.sec-sub{position:absolute;left:0;width:1216px;text-align:center;font-size:20px;color:var(--text)}

/* products */
.product{position:absolute;top:2455px;width:302px;height:245px;background:var(--card);border-radius:34px;text-align:center;overflow:hidden}
.product .tab{position:absolute;left:60px;top:-1px;width:150px;height:28px;background:var(--teal);border-radius:0 0 80px 80px/0 0 28px 28px}
.product svg{margin-top:38px}
.product h3{font-size:30px;font-weight:700;margin-top:8px}
.product p{font-size:17px;line-height:24px;color:var(--text);padding:4px 28px 0}

/* pricing */
.plan{position:absolute;top:2852px;width:302px;height:360px;background:var(--teal-pale);text-align:center;color:var(--ink)}
.plan.featured{background:var(--teal)}
.plan .price{margin-top:22px;font-size:55px;font-weight:700;line-height:1}
.plan .price small{font-size:15px;font-weight:400}
.plan h3{font-size:24px;font-weight:700;color:var(--white);margin-top:16px}
.plan .desc{font-size:13.5px;line-height:18px;padding:12px 24px 0}
.plan ul{list-style:none;font-size:14px;line-height:24.5px;margin-top:16px}
.plan .choose{display:inline-flex;align-items:center;justify-content:center;width:154px;height:39px;background:var(--white);font-size:14px;font-weight:700;margin-top:12px;color:var(--ink)}
.plan.featured .price,.plan.featured h3,.plan.featured .desc,.plan.featured ul{color:#a9c9c6}
.plan.featured .price{color:#9fc2bf}
.plan.featured .choose{background:#c5d2d2}

/* cta */
.cta{position:absolute;left:107px;top:3282px;width:985px;height:161px;border-radius:6px;background:linear-gradient(135deg,#1b1d1f 0%,#2a2c2f 50%,#151617 100%);text-align:center;color:var(--white)}
.cta h2{font-size:28px;font-weight:700;margin-top:26px}
.cta p{font-size:16px;color:#cfcfcf;margin-top:6px}
.cta a{display:inline-flex;align-items:center;justify-content:center;width:312px;height:44px;border:2px solid var(--white);border-radius:5px;font-size:26px;font-weight:700;margin-top:11px}

/* footer */
.footer{position:absolute;left:0;top:3484px;width:1200px;height:306px;background:var(--teal);color:var(--white)}
.footer .about{position:absolute;left:107px;top:155px;width:470px;font-size:18px;line-height:24px}
.socials{position:absolute;left:110px;top:214px;display:flex;gap:10px}
.socials span{width:30px;height:30px;border:3px solid var(--white);border-radius:6px}
.col-title{position:absolute;top:96px;font-size:23px;font-weight:700}
.links{position:absolute;left:597px;top:130px;list-style:none;font-size:14.5px;line-height:23px;letter-spacing:.5px}
.contact{position:absolute;left:801px;top:130px;list-style:none;font-size:14.5px;font-weight:700;letter-spacing:.5px}
.contact li{display:flex;align-items:center;gap:12px;height:30px}
.copy{position:absolute;left:0;top:250px;width:1200px;border-top:2px solid #3e8d87;padding-top:16px;text-align:center;font-size:12px}
</style>
</head>
<body>

<header class="hero">
  <div class="hero-bg" role="img" aria-label="Photo of two colleagues working together at a laptop in a dim office"></div>
  <svg class="hero-wave" width="1200" height="182" viewBox="0 0 1200 182" aria-hidden="true">
    <path d="M0 18 C180 80 420 178 640 178 C860 178 1040 60 1200 18 L1200 182 L0 182 Z" fill="#0d5f5a"/>
    <path d="M0 18 C180 80 420 168 640 164 C860 160 1040 70 1200 44 L1200 182 L0 182 Z" fill="#f5f5f5"/>
  </svg>
  <a class="brand" href="#" style="left:112px;top:24px"><span class="dot"></span>Lumen Grove</a>
  <nav class="nav">
    <a class="active" href="#">Home</a>
    <a href="#">About Us</a>
    <a href="#">Products</a>
    <a href="#">Pricing</a>
    <a href="#">How it works</a>
    <a href="#">Contact Us</a>
  </nav>
  <h1 class="hero-title">Cyber Security</h1>
  <p class="hero-sub">IS NOT OPTIONAL</p>
  <p class="hero-text">Lorem ipsum dolor sit amet, consectetur adipiscing elit, sed do eiusmod tempor incididunt ut labore et dolore magna aliqua. accumsan lacus vel facilisis.</p>
  <a class="btn-light" href="#">GET STARTED</a>
</header>

<section class="approach">
  <h2 class="approach-title">Our <span>Approach</span></h2>
  <p class="approach-sub">Is <span>Simple</span> But Not Time-Wasting</p>
  <div class="stat" style="left:712px;top:712px;width:161px;height:123px;background:var(--mist)"><b>12</b><small>Years Experience</small></div>
  <div class="stat" style="left:878px;top:760px;width:161px;height:125px;background:var(--sun)"><b>95</b><small>Customer Satisfaction</small></div>
  <div class="stat" style="left:712px;top:842px;width:161px;height:125px;background:var(--stone)"><b>38</b><small>Team Members</small></div>
  <div class="stat" style="left:878px;top:891px;width:161px;height:123px;background:var(--mist-2)"><b>321</b><small>Porject Complete</small></div>
</section>

<section class="about">
  <div class="about-panel"></div>
  <div class="about-photo" role="img" aria-label="Photo of a businessman in a suit holding a laptop"></div>
  <h2 class="about-title">About Us</h2>
  <p class="about-text">Lorem ipsum dolor sit amet, consectetur adipiscing elit, sed do eiusmod tempor incididunt ut labore et dolore magna aliqua. accumsan lacus vel facilisis.</p>
  <div class="feature" style="top:1232px"><h3>Highly Professional Members</h3><p>Lorem ipsum dolor sit amet, consectetur adipiscing elit, sed do eiusmod tempor incididunt ut labore et dolore magna aliqua.</p></div>
  <div class="feature" style="top:1414px"><h3>Infrastructure Integration Technology</h3><p>Lorem ipsum dolor sit amet, consectetur adipiscing elit, sed do eiusmod tempor incididunt ut labore et dolore magna aliqua.</p></div>
</section>

<section class="how">
  <h2 class="how-title">How it works</h2>
  <p class="how-text">Lorem ipsum dolor sit amet, consectetur adipiscing elit, sed do eiusmod tempor.</p>
  <div class="step" style="top:1866px"><h3>Company Analysis</h3><p>Lorem ipsum dolor sit amet, consectetur adipiscing elit, sed do eiusmod tempor</p></div>
  <div class="rule" style="top:1981px"></div>
  <div class="step" style="top:2000px"><h3>Specifications Listed</h3><p>Lorem ipsum dolor sit amet, consectetur adipiscing elit, sed do eiusmod tempor</p></div>
  <div class="rule" style="top:2113px"></div>
  <div class="step" style="top:2136px"><h3>Set up security</h3><p>Lorem ipsum dolor sit amet, consectetur adipiscing elit, sed do eiusmod tempor</p></div>
  <div class="how-photo" role="img" aria-label="Photo of a businessman on the phone blended with a night city skyline and network lines"></div>
</section>

<section class="products">
  <p class="eyebrow" style="top:2322px">Our Products</p>
  <h2 class="sec-title" style="top:2350px">Protect your space with the power of cybersafe</h2>
  <p class="sec-sub" style="top:2408px">Lorem ipsum dolor sit amet, consectetur adipiscing elit, do eiusmod.</p>

  <div class="product" style="left:107px"><div class="tab"></div>
    <svg width="64" height="64" viewBox="0 0 64 64" fill="none" stroke="#111" stroke-width="3"><circle cx="32" cy="32" r="22"/><circle cx="32" cy="28" r="7"/><path d="M32 35v10"/><circle cx="10" cy="32" r="3"/><circle cx="54" cy="32" r="3"/></svg>
    <h3>Cyber Security</h3><p>Lorem ipsum dolor sit amet, consectetur adipiscing elit, sed eiusmod amet elit.</p></div>
  <div class="product" style="left:451px"><div class="tab"></div>
    <svg width="64" height="64" viewBox="0 0 64 64" fill="none" stroke="#111" stroke-width="4"><circle cx="32" cy="32" r="26"/><circle cx="32" cy="32" r="18"/><path d="M22 32l8 8 18-20"/></svg>
    <h3>Data Protection</h3><p>Lorem ipsum dolor sit amet, consectetur adipiscing elit, sed eiusmod amet elit.</p></div>
  <div class="product" style="left:791px"><div class="tab"></div>
    <svg width="64" height="64" viewBox="0 0 64 64" fill="none" stroke="#111" stroke-width="3"><rect x="12" y="30" width="40" height="26" rx="4"/><path d="M20 30v-8a12 12 0 0 1 24 0v8"/><circle cx="24" cy="43" r="2" fill="#111"/><circle cx="32" cy="43" r="2" fill="#111"/><circle cx="40" cy="43" r="2" fill="#111"/></svg>
    <h3>Data Privacy</h3><p>Lorem ipsum dolor sit amet, consectetur adipiscing elit, sed eiusmod amet elit.</p></div>
</section>

<section class="pricing">
  <p class="eyebrow" style="top:2765px">Pricing Plan</p>
  <h2 class="sec-title" style="top:2788px;width:1200px">Security is just a click away</h2>

  <div class="plan" style="left:107px">
    <p class="price">$25<small>/ MONTHLY</small></p><h3>Basic Plan</h3>
    <p class="desc">Lorem ipsum dolor sit amet, consectetur adipiscing elit, sed eiusmod amet elit.</p>
    <ul><li>30 Days Product Testing</li><li>Upgrade Anytime Protection</li><li>500 Malware Removal</li><li>Configure Software One Time</li><li>24/7 Live Assistance</li></ul>
    <a class="choose" href="#">CHOOSE PLAN</a></div>
  <div class="plan featured" style="left:451px">
    <p class="price">$55<small>/ MONTHLY</small></p><h3>Standard Plan</h3>
    <p class="desc">Lorem ipsum dolor sit amet, consectetur adipiscing elit, sed eiusmod amet elit.</p>
    <ul><li>30 Days Product Testing</li><li>Upgrade Anytime Protection</li><li>500 Malware Removal</li><li>Configure Software One Time</li><li>24/7 Live Assistance</li></ul>
    <a class="choose" href="#">CHOOSE PLAN</a></div>
  <div class="plan" style="left:790px">
    <p class="price">$105<small>/ MONTHLY</small></p><h3>Premium Plan</h3>
    <p class="desc">Lorem ipsum dolor sit amet, consectetur adipiscing elit, sed eiusmod amet elit.</p>
    <ul><li>30 Days Product Testing</li><li>Upgrade Anytime Protection</li><li>500 Malware Removal</li><li>Configure Software One Time</li><li>24/7 Live Assistance</li></ul>
    <a class="choose" href="#">CHOOSE PLAN</a></div>
</section>

<section class="cta" role="region" aria-label="Call to action">
  <h2>Safeguarding Your Online Presence, Every Step of the Journey</h2>
  <p>Lorem ipsum dolor sit amet, consectetur adipiscing elit, do eiusmod.</p>
  <a href="#">GET STARTED</a>
</section>

<footer class="footer">
  <a class="brand" href="#" style="left:108px;top:44px"><span class="dot"></span>Lumen Grove</a>
  <p class="about">Lorem ipsum dolor sit amet, consectetur adipiscing elit, sed do eiusmod tempor incididunt ut labore.</p>
  <div class="socials" aria-label="Social links"><span></span><span></span><span></span></div>

  <h4 class="col-title" style="left:596px">Useful links</h4>
  <ul class="links"><li>About Us</li><li>Terms and conditions</li><li>privacy policy</li><li>How it works</li><li>Contact Us</li></ul>

  <h4 class="col-title" style="left:801px">Contact Us</h4>
  <ul class="contact">
    <li><svg width="20" height="20" viewBox="0 0 20 20" fill="none" stroke="#fff" stroke-width="2"><path d="M10 19s-6-6-6-10a6 6 0 0 1 12 0c0 4-6 10-6 10z"/><circle cx="10" cy="9" r="2"/></svg>Plaza 4, 2nd floor, Birch Street</li>
    <li><svg width="20" height="20" viewBox="0 0 20 20" fill="none" stroke="#fff" stroke-width="2"><path d="M4 2h4l1 5-2 1a10 10 0 0 0 5 5l1-2 5 1v4a2 2 0 0 1-2 2C9 18 2 11 2 4a2 2 0 0 1 2-2z"/></svg>+1-555-014-2290</li>
    <li><svg width="20" height="20" viewBox="0 0 20 20" fill="none" stroke="#fff" stroke-width="2"><rect x="2" y="4" width="16" height="12" rx="1"/><path d="M2 5l8 6 8-6"/></svg>hello@lumengrove.example</li>
  </ul>
  <p class="copy">Copyright © 2024 Lumen Grove. all rights reserved.</p>
</footer>

</body>
</html>
```